Business cards — need something that creates “wow” factor

Need a sleek and clean looking business card. Something that is clear and consise. These business cards are for my painting business and hundreds will be placed in the Dallas area between all Halverd Pemberton paint stored. These card really need to stick out! Open to any and all ideas...

Target Market(s)

Residential clientele

Industry/Entity Type

Painting

Contact Information for Business Card

Dorian Vakelby
Owner

382.516.2074

Web: Mesahuepainting.example (still under construction)
Mesahuepainting@mailbox.example

Font styles to use
Sans Serif

Colors

Designer to choose colors to be used in the design.

Requirements
Must have
• My name, number, website, email, Socialpage
• and “100% customer satisfaction guaranteed”
• Socialpage.example/Mesahuepainting/
Nice to have
• Listed services
• Interior/exterior painting
• Drywall repair/texture
• Fence staining/refinishing
• Concrete staining
• Epoxy flooring
• Pressure washing

```html
<!DOCTYPE html>
<html lang="en">
<head>
<meta charset="utf-8">
<title>Mesa Hue business cards</title>
<link rel="stylesheet" href="https://fonts.googleapis.com/css2?family=Arimo:wght@400;700&family=Montserrat:wght@700&display=swap">
<style>
  :root {
    --stage: #3a3a3c;
    --card: #1c1c1d;
    --ink: #f4f4f4;
    --muted: #8a8a8a;
    --teal: #1fb5b0;
    --spectrum: linear-gradient(90deg, #d0243a 0%, #e8632a 18%, #f1c232 36%, #6fbf44 52%, #1fb5b0 66%, #3b6fd1 80%, #8a3fc2 100%);
  }
  * { box-sizing: border-box; margin: 0; padding: 0; }
  html, body { width: 1200px; height: 1189px; overflow: hidden; }
  body {
    background: var(--stage);
    font-family: "Arimo", Arial, sans-serif;
    color: var(--ink);
    position: relative;
  }
  .card {
    position: absolute;
    left: 120px;
    width: 960px;
    height: 548px;
    background: var(--card);
    border-radius: 34px;
    box-shadow: 0 18px 40px rgba(0,0,0,.45);
  }
  .card--services { top: 36px; }
  .card--contact { top: 605px; }

  .brand { position: absolute; text-align: center; }
  .brand__mark {
    display: flex; align-items: center; justify-content: center; gap: 14px;
  }
  .brand__dot {
    width: 30px; height: 30px; border-radius: 50%;
    background: var(--ink);
  }
  .brand__name {
    font-size: 64px; font-weight: 400; letter-spacing: 3px;
    color: var(--ink); text-transform: uppercase;
  }
  .brand__tagline {
    margin-top: 8px; font-size: 13px; color: var(--muted); letter-spacing: .5px;
  }
  .card--services .brand { left: 0; right: 0; top: 130px; }
  .card--contact .brand { left: 60px; top: 70px; text-align: left; }
  .card--contact .brand__mark { justify-content: flex-start; }

  .services {
    position: absolute; left: 40px; right: 40px; top: 330px;
    text-align: center; font-size: 24px; line-height: 1.55;
  }
  .services .sep { color: var(--teal); padding: 0 6px; }
  .guarantee {
    position: absolute; left: 0; right: 0; top: 450px;
    text-align: center; font-size: 18px; font-weight: 700;
    letter-spacing: 1px; color: var(--teal); text-transform: uppercase;
  }

  .spectrum-line {
    position: absolute; left: 60px; right: 160px; top: 300px;
    height: 2px; background: var(--spectrum);
  }
  .person__name {
    position: absolute; right: 130px; top: 258px;
    font-family: "Montserrat", Arial, sans-serif; font-weight: 700; font-size: 28px;
  }
  .person__role {
    position: absolute; right: 90px; top: 288px; font-size: 20px;
    background: var(--spectrum); -webkit-background-clip: text; background-clip: text; color: transparent;
  }
  .address {
    position: absolute; right: 70px; top: 350px; text-align: right;
    font-size: 24px; line-height: 1.3;
  }
  .contact { position: absolute; left: 60px; top: 350px; list-style: none; }
  .contact li {
    display: flex; align-items: center; gap: 12px;
    font-size: 24px; line-height: 1; margin-bottom: 12px;
  }
  .contact__icon {
    flex: none;
    width: 28px; height: 28px; border-radius: 50%;
    background: var(--spectrum);
    display: flex; align-items: center; justify-content: center;
  }
</style>
</head>
<body>
  <section class="card card--services">
    <div class="brand">
      <div class="brand__mark"><span class="brand__dot"></span><span class="brand__name">Mesa Hue</span></div>
      <p class="brand__tagline">Commercial | Residential | Interior | Exterior</p>
    </div>
    <p class="services">
      Interior/exterior painting<span class="sep">|</span>Drywall repair/texture<span class="sep">|</span>Fence staining/refinishing<br>
      Concrete staining<span class="sep">|</span>Epoxy flooring<span class="sep">|</span>Pressure washing
    </p>
    <p class="guarantee">100% customer satisfaction guaranteed</p>
  </section>

  <section class="card card--contact">
    <div class="brand">
      <div class="brand__mark"><span class="brand__dot"></span><span class="brand__name">Mesa Hue</span></div>
      <p class="brand__tagline">Commercial | Residential | Interior | Exterior</p>
    </div>
    <p class="person__name">Dorian Vakelby</p>
    <div class="spectrum-line"></div>
    <p class="person__role">Owner</p>
    <p class="address">PO BOX 480 Larkspur Lane<br>Unit 2</p>
    <ul class="contact">
      <li><span class="contact__icon"><svg width="16" height="16" viewBox="0 0 16 16"><path d="M4 1.5l2.5 3-1.5 1.6a9 9 0 0 0 4.9 4.9l1.6-1.5 3 2.5-1.6 2.2C7.5 14.5 1.5 8.5 1.8 3.1z" fill="#fff"/></svg></span>382.516.2074</li>
      <li><span class="contact__icon"><svg width="16" height="16" viewBox="0 0 16 16"><rect x="1.5" y="3.5" width="13" height="9" fill="none" stroke="#fff" stroke-width="1.5"/><path d="M1.5 3.5L8 9l6.5-5.5" fill="none" stroke="#fff" stroke-width="1.5"/></svg></span>Mesahuepainting@mailbox.example</li>
      <li><span class="contact__icon"><svg width="16" height="16" viewBox="0 0 16 16"><g fill="none" stroke="#fff" stroke-width="1.3"><circle cx="8" cy="8" r="6.3"/><ellipse cx="8" cy="8" rx="2.8" ry="6.3"/><path d="M1.7 8h12.6"/></g></svg></span>Mesahuepainting.example</li>
      <li><span class="contact__icon"><svg width="16" height="16" viewBox="0 0 16 16"><g fill="none" stroke="#fff" stroke-width="1.5"><rect x="1.5" y="5.5" width="7" height="5" rx="2.5"/><rect x="7.5" y="5.5" width="7" height="5" rx="2.5"/></g></svg></span>Socialpage.example/Mesahuepainting/</li>
    </ul>
  </section>
</body>
</html>
```